E-book named 'Harbourlight: A Field Manual for Purpose Builders' needs cover

I need a cover for my ebook and also paper back book.
I need a very appealing cover for my ebook. Social enterprise is a company that gives something back to the society as opposed to only make profit.
The society and its people always benefit.
So far the above is the name chosen but I welcome small changes and ideas also a tag line would also be great something like “everything you need to know to sep up a social enterprise and succeed”
I want to write in the cover something to make people buy it. I want the name Social Enterprise in more evidence ...
Target Market(s)
Students, graduates and business minded people who are thinking of set up a social enterprise company and needs guidance
Industry/Entity Type
It Company
Colors
Designer to choose colors to be used in the design.
Look and feel
Each slider illustrates characteristics of the customer's brand and the style your logo design should communicate.

```html
<!DOCTYPE html>
<html lang="en">
<head>
<meta charset="utf-8">
<title>Harbourlight: A Field Manual for Purpose Builders — Cover</title>
<link rel="stylesheet" href="https://fonts.googleapis.com/css2?family=Bebas+Neue&family=Oswald:wght@500;600&family=Roboto+Condensed:wght@400&family=Roboto:wght@400&display=swap">
<style>
  :root {
    --backdrop: #c4c4c4;
    --paper: #ffffff;
    --paper-shade: #f3f3f3;
    --ink: #1e1e1e;
    --green: #2bb54a;
    --green-light: #9fd33a;
    --green-pale: #d8ef9a;
  }
  * { margin: 0; padding: 0; box-sizing: border-box; }
  html, body {
    width: 1200px;
    height: 960px;
    overflow: hidden;
    background: var(--backdrop);
  }
  .canvas {
    position: relative;
    width: 1200px;
    height: 960px;
  }
  .cover {
    position: absolute;
    left: 300px;
    top: 30px;
    width: 600px;
    height: 900px;
    background: linear-gradient(180deg, var(--paper) 0%, var(--paper-shade) 100%);
    text-align: center;
    color: var(--ink);
  }
  .cover__kicker {
    position: absolute;
    top: 48px;
    left: 0;
    right: 0;
    font-family: "Oswald", sans-serif;
    font-weight: 600;
    font-size: 30px;
    letter-spacing: 1px;
  }
  .cover__title {
    position: absolute;
    top: 96px;
    left: 0;
    right: 0;
    font-family: "Bebas Neue", sans-serif;
    font-weight: 400;
    color: var(--green);
    line-height: 0.98;
  }
  .cover__title-line { display: block; }
  .cover__title-line--first { font-size: 112px; }
  .cover__title-line--second { font-size: 80px; }
  .cover__tagline {
    position: absolute;
    top: 328px;
    left: 0;
    right: 0;
    font-family: "Roboto Condensed", sans-serif;
    font-size: 24px;
    line-height: 1.35;
  }
  .cover__illustration {
    position: absolute;
    left: 140px;
    top: 420px;
    width: 320px;
    height: 340px;
    border-radius: 50%;
    background: radial-gradient(circle at 50% 50%, var(--paper) 0%, var(--paper) 46%, var(--green-pale) 52%, var(--green-light) 68%, var(--green) 90%, rgba(43,181,74,0) 100%);
  }
  .cover__author {
    position: absolute;
    top: 820px;
    left: 0;
    right: 0;
    font-family: "Roboto", sans-serif;
    font-size: 42px;
    letter-spacing: 10px;
    padding-left: 10px;
  }
</style>
</head>
<body>
  <main class="canvas">
    <section class="cover">
      <p class="cover__kicker">HARBOURLIGHT</p>
      <h1 class="cover__title">
        <span class="cover__title-line cover__title-line--first">A FIELD MANUAL</span>
        <span class="cover__title-line cover__title-line--second">FOR PURPOSE BUILDERS</span>
      </h1>
      <p class="cover__tagline">Everything You Need to Know to<br>Set Up a Social Enterprise and Succeed</p>
      <div class="cover__illustration" role="img" aria-label="Green illustration of a small round planet ringed by city buildings, trees, a ferris wheel, cyclists and walkers"></div>
      <p class="cover__author">AUTHOR NAME</p>
    </section>
  </main>
</body>
</html>
```